New Dental Office Needs an Attractive and user friendly Website Designed

I need a website for a new dental office. The Name is Maplecrest Dentistry. I would like a Modern design with a user friendly interface and usability.
I would like a landing page, a page that lists the services we offer: Cosmetic Dentistry, Implants, Dental Hygiene, Emergency Services, Restorations, Dentures
Target Market(s)
Mid to upper class
Industry/Entity Type
Dentistry
Coding
Coded - Design and coding required
Number of Pages Required
1 page
Requirements
Must have
- Landing page that has a scheduling option, Procedures, operating hours, and contact us info
Nice to have
- Appealing design, Soft comforting colors. Easy to navigate page, Modern and professional.

```html
<!DOCTYPE html>
<html lang="en">
<head>
<meta charset="utf-8">
<title>Maplecrest Dentistry</title>
<link href="https://fonts.googleapis.com/css2?family=Playfair+Display:wght@400;500&family=Poppins:wght@400;500;600&display=swap" rel="stylesheet">
<style>
:root{
  --teal:#1f7a7b;
  --teal-dark:#176465;
  --orange:#d08a66;
  --cream:#fbf8f1;
  --card:#eef0ea;
  --ink:#2b2b2b;
  --muted:#555;
  --dark:#262626;
  --line:#cfcfcf;
}
*{box-sizing:border-box;margin:0;padding:0}
html,body{width:1200px;height:3436px;overflow:hidden}
body{position:relative;background:var(--cream);font-family:"Poppins",sans-serif;color:var(--ink)}
.abs{position:absolute}
.serif{font-family:"Playfair Display",serif;font-weight:400}
.btn{position:absolute;display:flex;align-items:center;justify-content:center;gap:14px;font-size:12px;font-weight:600;letter-spacing:.3px;border-radius:3px;text-transform:uppercase;white-space:nowrap;text-decoration:none}
.btn::after{content:"";width:6px;height:6px;border-radius:50%;background:currentColor}
.btn.no-dot::after{display:none}
.btn-teal{background:var(--teal);color:#fff}
.btn-white{background:#fff;color:var(--ink)}
.btn-white::after{background:var(--teal)}

/* hero */
.hero-photo{left:0;top:0;width:1200px;height:660px;background:
  radial-gradient(ellipse 260px 300px at 860px 200px,rgba(226,200,184,.85),rgba(226,200,184,0) 70%),
  radial-gradient(ellipse 200px 240px at 470px 170px,rgba(170,140,120,.55),rgba(170,140,120,0) 70%),
  radial-gradient(ellipse 380px 200px at 760px 470px,rgba(95,120,170,.6),rgba(95,120,170,0) 70%),
  linear-gradient(110deg,#2f6f74 0%,#4f8a8d 30%,#9fb5b4 55%,#c9cfcb 75%,#8fa4a3 100%)}
.brand{font-family:"Playfair Display",serif;font-size:24px;color:#fff;line-height:1;white-space:nowrap}
.nav a{position:absolute;top:37px;color:#fff;font-size:11px;font-weight:500;text-decoration:none;text-transform:uppercase}
.hero-kicker{left:136px;top:222px;color:#fff;font-size:18px;font-weight:600}
.hero-title{left:136px;top:244px;color:#fff;font-size:72px;line-height:82px}

/* services */
.section-title{width:1200px;left:0;text-align:center;font-size:34px}
.svc{position:absolute;top:772px;width:216px;text-align:center}
.svc-photo{width:216px;height:216px;border-radius:50%;border:10px solid #f1ebe0}
.ph-cosmetic{background:radial-gradient(circle at 55% 65%,#f4efe9 0 12%,rgba(244,239,233,0) 26%),radial-gradient(circle at 40% 40%,#e2b9a8,#b67c6b 60%,#7d5247)}
.ph-hygiene{background:radial-gradient(circle at 60% 70%,#c9524f 0 8%,rgba(201,82,79,0) 22%),radial-gradient(circle at 35% 35%,#9aa3a8 0 10%,rgba(154,163,168,0) 28%),radial-gradient(circle,#d9a792,#a66d5c 65%,#6f463c)}
.ph-emergency{background:radial-gradient(circle at 60% 72%,#ffffff 0 14%,rgba(255,255,255,0) 30%),radial-gradient(circle at 35% 35%,#f6f7f8,#dde4e8 55%,#b4c2cb)}
.ph-restore{background:radial-gradient(circle at 55% 55%,#f3eee6 0 10%,rgba(243,238,230,0) 24%),radial-gradient(circle at 75% 80%,#3d6fb0 0 8%,rgba(61,111,176,0) 22%),radial-gradient(circle,#d4937c,#a35f4d 65%,#6c3d33)}
.ph-gray{background:radial-gradient(circle at 45% 45%,#f1f3f3,#c6cdcf 60%,#9aa5a8)}
.svc-badge{position:absolute;left:84px;top:-6px;width:48px;height:48px;border-radius:50%;background:var(--orange);border:3px solid #fff;display:flex;align-items:center;justify-content:center}
.svc-name{margin-top:14px;font-family:"Playfair Display",serif;font-size:20px;white-space:nowrap}
.watermark{left:0;width:1200px;font-size:100px;font-weight:500;white-space:nowrap;color:transparent;-webkit-text-stroke:1px rgba(0,0,0,.07);letter-spacing:2px;overflow:hidden;line-height:1}

/* about */
.about-photo{left:0;top:1181px;width:1200px;height:484px;background:
  radial-gradient(ellipse 110px 190px at 810px 340px,rgba(255,255,255,.95),rgba(255,255,255,0) 75%),
  radial-gradient(ellipse 110px 190px at 970px 330px,rgba(255,255,255,.95),rgba(255,255,255,0) 75%),
  radial-gradient(ellipse 50px 60px at 820px 135px,rgba(140,95,70,.7),rgba(140,95,70,0) 80%),
  radial-gradient(ellipse 50px 60px at 975px 125px,rgba(120,80,55,.7),rgba(120,80,55,0) 80%),
  radial-gradient(ellipse 150px 70px at 640px 420px,rgba(70,120,175,.45),rgba(70,120,175,0) 75%),
  linear-gradient(90deg,#f3ede2 0%,#ede6d8 40%,#dfe0da 60%,#d0d7d6 100%)}
.about-card{left:147px;top:1237px;width:387px;height:408px;background:rgba(236,226,204,.75);padding:44px 32px}
.about-card h2{font-size:34px;line-height:42px;margin-bottom:20px}
.about-card p{font-size:12px;line-height:18px;color:#444}

/* why */
.why{left:0;top:1665px;width:1200px;height:320px;background:var(--orange)}
.why-title{color:#fff;font-size:32px;top:46px}
.why-item{position:absolute;top:118px;width:260px;text-align:center;color:#fbe9de;font-family:"Playfair Display",serif;font-size:17px;line-height:22px}
.why-icon{width:78px;height:78px;margin:0 auto 18px;border-radius:50%;background:#fff;border:5px solid #e7ad8f;display:flex;align-items:center;justify-content:center}

/* reviews */
.rule{height:1px;background:var(--line)}
.review{position:absolute;top:2131px;width:306px;height:216px;background:var(--card);border-radius:4px;padding:22px 20px;font-size:11px;line-height:17px;color:#444}
.review .stars{color:#f4b400;font-size:15px;letter-spacing:2px;display:flex;align-items:center;gap:6px}
.review .dot{width:16px;height:16px;border-radius:50%;background:#4a8be0;display:inline-block}
.review .quote{position:absolute;right:16px;top:0;font-family:"Playfair Display",serif;font-size:90px;color:#d7dcd6;line-height:1}
.review .date{margin:6px 0 6px;font-size:11px}
.review .who{position:absolute;left:20px;bottom:18px;display:flex;align-items:center;gap:10px;font-weight:500;color:var(--ink);font-size:12px}
.avatar{width:34px;height:34px;border-radius:50%;background:#d9c1b1;border:2px solid #fff}
.arrow{width:22px;height:22px;border-radius:50%;border:1px solid #555;display:flex;align-items:center;justify-content:center}

/* locations */
.loc-photo{width:142px;height:133px;border:3px solid #fff;box-shadow:0 0 0 1px #ddd}
.loc-a{background:linear-gradient(135deg,#d7d9db 0%,#8d969c 50%,#4f585e 100%)}
.loc-b{background:linear-gradient(135deg,#f2f3f4 0%,#c3cbd2 50%,#4c6a86 100%)}
.loc-c{background:linear-gradient(135deg,#a9c2d6 0%,#e6eaed 50%,#5e6f7c 100%)}
.loc-d{background:linear-gradient(135deg,#dfe4e8 0%,#9fb0bd 50%,#4f6272 100%)}
.loc-text h3{font-family:"Playfair Display",serif;font-weight:400;font-size:18px}
.loc-text .ph{font-size:14px;margin:2px 0 10px}
.loc-text .ad{font-size:11px;line-height:18px}
.loc-text a{display:inline-block;margin-top:6px;font-size:12px;font-weight:600;color:var(--teal)}
.right{text-align:right}

/* cta */
.cta{left:253px;top:2897px;width:694px;height:225px;background:var(--teal);text-align:center;color:#fff}
.cta h2{font-size:34px;line-height:33px;margin-top:34px}
.cta p{font-size:12px;margin-top:10px}

/* footer */
.footer{left:0;top:3120px;width:1200px;height:316px;background:var(--dark);color:#fff}
.fcol h4{font-family:"Playfair Display",serif;font-weight:400;font-size:18px;margin-bottom:14px}
.fcol li{list-style:none;font-size:9px;line-height:19px}
.fline{display:flex;align-items:center;gap:12px;font-size:9px;margin-bottom:14px}
.ficon{width:20px;height:20px;border-radius:50%;background:#fff;display:flex;align-items:center;justify-content:center;flex:none}
.vdiv{position:absolute;top:40px;width:1px;height:190px;background:#555}
</style>
</head>
<body>

<!-- HERO -->
<div class="abs hero-photo" role="img" aria-label="Smiling senior patient in a dental chair with her dentist behind her"></div>
<svg class="abs" style="left:0;top:0" width="1200" height="700" viewBox="0 0 1200 700">
  <path d="M0 585 C160 640 300 672 470 658 C700 640 860 520 1000 470 C1080 442 1150 445 1200 455 L1200 700 L0 700 Z" fill="var(--cream)"/>
  <path d="M0 585 C160 640 300 672 470 658 C700 640 860 520 1000 470 C1080 442 1150 445 1200 455" fill="none" stroke="var(--teal)" stroke-width="8"/>
</svg>
<div class="abs brand" style="left:120px;top:38px">Maplecrest Dentistry</div>
<nav class="nav">
  <a style="left:402px">Services</a>
  <a style="left:485px">About Us</a>
  <a style="left:571px">Locations</a>
  <a style="left:665px">FAQs</a>
  <a style="left:724px">Contact Us</a>
</nav>
<a class="btn btn-teal" style="left:871px;top:24px;width:207px;height:36px">Request an Appointment</a>
<div class="abs hero-kicker">Your Trusted Maplecrest Dentistry</div>
<h1 class="abs serif hero-title">Healthy Teeth,<br>Happy Smiles.</h1>
<a class="btn btn-white" style="left:136px;top:430px;width:262px;height:41px">Book Your Appointment Today</a>

<!-- SERVICES -->
<h2 class="abs serif section-title" style="top:688px">Services We Offer</h2>
<div class="svc" style="left:-118px"><div class="svc-photo ph-gray" role="img" aria-label="Denture model"></div><div class="svc-name" style="text-align:right">Dentures</div></div>
<div class="svc" style="left:125px"><div class="svc-photo ph-cosmetic" role="img" aria-label="Close-up of a smile during a cosmetic exam"></div><div class="svc-badge"><svg width="22" height="22" viewBox="0 0 24 24" fill="none" stroke="#fff" stroke-width="1.6"><circle cx="12" cy="12" r="8"/></svg></div><div class="svc-name">Cosmetic Dentistry</div></div>
<div class="svc" style="left:369px"><div class="svc-photo ph-hygiene" role="img" aria-label="Dental hygiene cleaning"></div><div class="svc-badge"><svg width="22" height="22" viewBox="0 0 24 24" fill="none" stroke="#fff" stroke-width="1.6"><circle cx="12" cy="12" r="8"/><path d="M12 8v8M8 12h8"/></svg></div><div class="svc-name">Dental Hygiene</div></div>
<div class="svc" style="left:614px"><div class="svc-photo ph-emergency" role="img" aria-label="Tooth with an ambulance for emergency care"></div><div class="svc-badge"><svg width="22" height="22" viewBox="0 0 24 24" fill="none" stroke="#fff" stroke-width="1.6"><rect x="3" y="7" width="18" height="11" rx="2"/><path d="M12 9v6M9 12h6"/></svg></div><div class="svc-name">Emergency Services</div></div>
<div class="svc" style="left:857px"><div class="svc-photo ph-restore" role="img" aria-label="Smile with shade guide for restorations"></div><div class="svc-badge"><svg width="22" height="22" viewBox="0 0 24 24" fill="none" stroke="#fff" stroke-width="1.6"><circle cx="12" cy="12" r="8"/><circle cx="12" cy="12" r="3"/></svg></div><div class="svc-name">Restorations</div></div>
<div class="svc" style="left:1106px"><div class="svc-photo ph-gray" role="img" aria-label="Dental implant model"></div><div class="svc-name" style="text-align:left;padding-left:58px">Implants</div></div>
<a class="btn btn-teal" style="left:519px;top:1059px;width:162px;height:41px">View All Services</a>
<div class="abs watermark" style="top:1098px">MAPLECREST DENTISTRY</div>

<!-- ABOUT -->
<div class="abs about-photo" role="img" aria-label="Two smiling dentists in white coats in a treatment room"></div>
<div class="abs about-card">
  <h2 class="serif">About Maplecrest Dentistry</h2>
  <p>Welcome to Maplecrest Family Dentistry. Born in this area, Dr. Owen Hartley has always had a desire to return to Alder County. Today he is pleased to offer high-quality dental care to friends and neighbors in Alder Center. He believes in giving back and is an engaged member of our community.</p>
</div>
<a class="btn btn-teal" style="left:178px;top:1510px;width:262px;height:41px">Book Your Appointment Today</a>

<!-- WHY -->
<section class="abs why">
  <h2 class="abs serif section-title why-title">Why Choose Us Maplecrest Dentistry?</h2>
  <div class="why-item" style="left:103px"><div class="why-icon"><svg width="38" height="38" viewBox="0 0 40 40" fill="none" stroke="#555" stroke-width="1.6"><circle cx="20" cy="16" r="10"/><circle cx="20" cy="16" r="5"/><path d="M14 24l-4 10 5-2 3 4 2-8M26 24l4 10-5-2-3 4-2-8"/></svg></div>Best-in<br>Class Dentists</div>
  <div class="why-item" style="left:344px"><div class="why-icon"><svg width="38" height="38" viewBox="0 0 40 40" fill="none" stroke="#555" stroke-width="1.6"><circle cx="20" cy="20" r="13"/><rect x="13" y="23" width="14" height="6" rx="1"/><path d="M12 18a8 8 0 0 1 16 0"/></svg></div>Modern care &amp;<br>Technology focused on You</div>
  <div class="why-item" style="left:606px"><div class="why-icon"><svg width="38" height="38" viewBox="0 0 40 40" fill="none" stroke="#555" stroke-width="1.6"><rect x="8" y="10" width="24" height="22" rx="2"/><path d="M8 16h24M14 7v6M26 7v6M15 24l4 4 7-7"/></svg></div>Evening and<br>Weekend Appointments</div>
  <div class="why-item" style="left:835px"><div class="why-icon"><svg width="38" height="38" viewBox="0 0 40 40" fill="none" stroke="#555" stroke-width="1.6"><circle cx="20" cy="20" r="13"/><path d="M17 12h6v5h5v6h-5v5h-6v-5h-5v-6h5z"/></svg></div>Only the<br>Care You need</div>
</section>

<!-- REVIEWS -->
<div class="abs rule" style="left:121px;top:2048px;width:958px"></div>
<div class="abs rule" style="left:121px;top:2107px;width:958px"></div>
<h2 class="abs serif" style="left:143px;top:2054px;font-size:34px">What Our Clients Say About Us</h2>
<div class="abs" style="left:753px;top:2054px;font-size:14px;font-weight:600;white-space:nowrap">ReviewHub <span style="font-weight:500">Reviews</span></div>
<div class="abs" style="left:753px;top:2076px;font-size:15px;font-weight:600;white-space:nowrap">5.0 <span style="color:#f4b400;letter-spacing:1px">★★★★★</span> <span style="font-size:9px;color:#999;font-weight:400">(223)</span></div>
<a class="btn btn-teal no-dot" style="left:910px;top:2060px;width:168px;height:38px;text-transform:none;font-size:11px">Review us on ReviewHub</a>
<div class="abs arrow" style="left:88px;top:2227px"><svg width="10" height="10" viewBox="0 0 10 10"><path d="M6 2L3 5l3 3" fill="none" stroke="#444" stroke-width="1.3"/></svg></div>
<div class="abs arrow" style="left:1090px;top:2227px"><svg width="10" height="10" viewBox="0 0 10 10"><path d="M4 2l3 3-3 3" fill="none" stroke="#444" stroke-width="1.3"/></svg></div>
<div class="review" style="left:123px"><span class="quote">”</span><div class="stars"><span class="dot"></span>★★★★★</div><div class="date">26 February 2025</div><p>What a great dental office. By far the best customer service. My kids enjoyed their dental visit. Thank you Maplecrest Dentistry.</p><div class="who"><span class="avatar"></span>Clara Winslow</div></div>
<div class="review" style="left:448px"><span class="quote">”</span><div class="stars"><span class="dot"></span>★★★★★</div><div class="date">26 February 2025</div><p>The best dentist ever! Everyone is nice, doctor is skilled, and I was helped immediately. They helped me with my anxiety. I also loved the dog Ollie! Thank you very much.</p><div class="who"><span class="avatar"></span>Jordan P.</div></div>
<div class="review" style="left:773px"><span class="quote">”</span><div class="stars"><span class="dot"></span>★★★★★</div><div class="date">26 February 2025</div><p>Dr. Hartley is fantastic. I switched to his dentist office recently and have had my teeth cleaned and also invisible liners. I couldn't be more happy with the service I've received from Dr. Hartley and the team there.</p><div class="who"><span class="avatar"></span>Elise T.</div></div>
<div class="abs watermark" style="top:2372px">MAPLECREST DENTISTRY</div>

<!-- LOCATIONS -->
<h2 class="abs serif section-title" style="top:2468px">Our Location</h2>
<div class="abs rule" style="left:121px;top:2535px;width:958px;background:#999"></div>
<div class="abs rule" style="left:121px;top:2835px;width:958px;background:#999"></div>
<div class="abs" role="img" aria-label="Street map showing the clinic location" style="left:440px;top:2545px;width:340px;height:280px;background:radial-gradient(ellipse at center,#eeeeea 0%,#f6f4ee 70%,var(--cream) 100%)"></div>
<div class="abs serif" style="left:510px;top:2602px;width:150px;height:52px;background:#fff;border:1px solid #ddd;display:flex;align-items:center;justify-content:center;font-size:17px;text-align:center;line-height:18px">Maplecrest<br>Dentistry</div>
<svg class="abs" style="left:567px;top:2666px" width="34" height="42" viewBox="0 0 34 42"><path d="M17 40C17 40 3 24 3 15a14 14 0 0 1 28 0c0 9-14 25-14 25z" fill="#fff" stroke="#222" stroke-width="2.5"/><circle cx="17" cy="15" r="5" fill="#222"/></svg>

<div class="abs loc-photo loc-a" style="left:123px;top:2542px" role="img" aria-label="Treatment room with dental chair"></div>
<div class="abs loc-text" style="left:283px;top:2548px"><h3>Briarwood</h3><div class="ph">(555) 214-0187</div><div class="ad">118 N Briarwood Dr.<br>Briarwood, IL 60099</div><a>Get directions</a></div>
<div class="abs loc-photo loc-b" style="left:123px;top:2691px" role="img" aria-label="Bright treatment room with dental chair"></div>
<div class="abs loc-text" style="left:283px;top:2697px"><h3>Cedar Park</h3><div class="ph">(555) 318-2290</div><div class="ad">4420 Grand Ave.<br>Cedar Park, IL 60077</div><a>Get directions</a></div>
<div class="abs loc-photo loc-c" style="left:936px;top:2542px" role="img" aria-label="Modern dental operatory"></div>
<div class="abs loc-text right" style="right:282px;top:2546px"><h3>Alder Center</h3><div class="ph">(555) 214-0187</div><div class="ad">118 N Briarwood Dr.<br>Briarwood, IL 60099</div><a>Get directions</a></div>
<div class="abs loc-photo loc-d" style="left:936px;top:2691px" role="img" aria-label="Dental chair by a window"></div>
<div class="abs loc-text right" style="right:282px;top:2697px"><h3>Briarwood</h3><div class="ph">(555) 214-0187</div><div class="ad">118 N Briarwood Dr.<br>Briarwood, IL 60099</div><a>Get directions</a></div>

<!-- CTA + FOOTER -->
<svg class="abs" style="left:0;top:2940px" width="1200" height="200" viewBox="0 0 1200 200">
  <path d="M0 182 C250 150 500 60 800 60 C980 60 1100 100 1200 150 L1200 200 L0 200 Z" fill="var(--dark)"/>
  <path d="M0 182 C250 150 500 60 800 60 C980 60 1100 100 1200 150" fill="none" stroke="var(--teal)" stroke-width="10"/>
</svg>
<div class="abs" role="img" aria-label="Decorative teal leaves" style="left:105px;top:2945px;width:220px;height:180px;border-radius:50% 50% 40% 40%;background:radial-gradient(circle,rgba(31,122,123,.55),rgba(31,122,123,0) 70%)"></div>
<div class="footer abs">
  <div class="abs fcol" style="left:121px;top:52px"><h4>Contact Us</h4>
    <div class="fline"><span class="ficon"><svg width="11" height="11" viewBox="0 0 12 12"><rect x="1" y="3" width="10" height="7" fill="none" stroke="#262626"/><path d="M1 3l5 4 5-4" fill="none" stroke="#262626"/></svg></span><span style="color:#4fb3b3">hello@maplecrestdental.com</span></div>
    <div class="fline"><span class="ficon"><svg width="11" height="11" viewBox="0 0 12 12"><path d="M2 1l2 0 1 3-1 1a7 7 0 0 0 3 3l1-1 3 1v2a1 1 0 0 1-1 1C5 11 1 7 1 2a1 1 0 0 1 1-1z" fill="#262626"/></svg></span>(555) 402-7715</div>
    <div class="fline"><span class="ficon"><svg width="11" height="11" viewBox="0 0 12 12"><rect x="2" y="5" width="8" height="5" fill="#262626"/><rect x="3" y="1" width="6" height="4" fill="none" stroke="#262626"/></svg></span>(555) 402-7715</div>
  </div>
  <div class="vdiv" style="left:287px"></div>
  <div class="abs fcol" style="left:312px;top:52px"><h4>Hours</h4>
    <div style="display:flex;gap:12px"><span class="ficon"><svg width="12" height="12" viewBox="0 0 12 12"><circle cx="6" cy="6" r="5" fill="none" stroke="#262626"/><path d="M6 3v3l2 1" fill="none" stroke="#262626"/></svg></span>
    <ul><li>Monday 7:30AM - 4:30PM</li><li>Tuesday 7:30AM - 4:30PM</li><li>Wednesday 7:30AM - 4:30PM</li><li>Thursday Closed</li><li>Friday 7:30AM - 3:00PM</li><li>Saturday Closed</li><li>Sunday Closed</li></ul></div>
  </div>
  <div class="vdiv" style="left:488px"></div>
  <div class="abs fcol" style="left:532px;top:52px"><h4>Main Links</h4>
    <ul><li>Home</li><li>Services</li><li>About Us</li><li>Locations</li><li>FAQ</li><li>Contact Us</li></ul></div>
  <div class="vdiv" style="left:673px"></div>
  <div class="abs fcol" style="left:713px;top:52px"><h4>Follow Us</h4>
    <div class="fline"><span class="ficon"></span>Circlefeed</div>
    <div class="fline"><span class="ficon"></span>Workline</div>
    <div class="fline"><span class="ficon"></span>Chirper</div></div>
  <div class="vdiv" style="left:863px"></div>
  <div class="abs fcol" style="left:903px;top:52px"><h4>Subscribe Newsletter</h4>
    <div style="width:163px;height:36px;border:1px solid #888;border-radius:3px;font-size:9px;display:flex;align-items:center;padding-left:16px">Enter Your Email</div>
  </div>
  <a class="btn btn-teal" style="left:905px;top:134px;width:161px;height:40px;justify-content:space-between;padding:0 18px">Subscribe</a>
  <div class="abs" style="left:112px;top:232px;width:976px;height:1px;background:#555"></div>
  <div class="abs" style="left:121px;top:264px;font-size:8px">© Maplecrest Dentistry 2025 All Rights Reserved</div>
  <div class="abs brand" style="left:0;width:1200px;text-align:center;top:256px">Maplecrest Dentistry</div>
  <div class="abs" style="right:124px;top:266px;font-size:8px">Privacy Policy | Website Terms Of Use</div>
</div>

<section class="abs cta">
  <h2 class="serif">Give us a call to Schedule<br>Your next Appointment.</h2>
  <p>Ready to Experience Pain-free Maplecrest Dentistry</p>
</section>
<a class="btn btn-white" style="left:421px;top:3034px;width:190px;height:40px">Request Appointment</a>
<div class="abs" style="left:624px;top:3040px;display:flex;align-items:center;gap:8px;color:#fff;font-size:17px;white-space:nowrap">
  <span class="ficon"><svg width="11" height="11" viewBox="0 0 12 12"><path d="M2 1l2 0 1 3-1 1a7 7 0 0 0 3 3l1-1 3 1v2a1 1 0 0 1-1 1C5 11 1 7 1 2a1 1 0 0 1 1-1z" fill="var(--teal)"/></svg></span>(555) 402-7715
</div>

</body>
</html>
```